Vellorine Baby Collection

We are creating the label for baby skin care products for our existing skin care brand called Vellorine. we want to play on sophistication of Vellorine current labelling and change to include kids/baby look and feel but keeping the up market style. We will have full range of different products like
1.Shampoo and Body Wash
2. Healing Cream
3. Nappy Rush Cream
4. Baby Massage Gel
5.Baby Bubble Bath
6.Baby Soothing Skin Lotion

Target Market(s)

Our target market are customers in Australia and Asia looking to purchase quality skin care products for their new born babies and young children

Industry/Entity Type

Skin care

Requirements
Must have
• some children look combined with an existing Vellorine brand
Nice to have
• maybe some baby toys and letters around the main name Vellorine

```html
<!DOCTYPE html>
<html lang="en">
<head>
<meta charset="utf-8">
<title>Vellorine Baby Collection – Labels</title>
<link rel="stylesheet" href="https://fonts.googleapis.com/css2?family=Fredoka:wght@500;600;700&family=Tenor+Sans&display=swap">
<style>
  :root {
    --bg: #d3ebf1;
    --label-white: #f7f6f7;
    --brand-ink: #6b2a86;
    --plum: #8a2f6e;
    --plum-band: #7a2f78;
    --cyan: #27b6d4;
    --cyan-deep: #1aa2c4;
    --cyan-band: #33bedb;
    --pink-dot: #f06cb4;
    --blue-dot: #2fb3e4;
    --bear-light: #f0d3a4;
    --bear-mid: #d9b07a;
    --text-white: #ffffff;
  }
  * { box-sizing: border-box; margin: 0; padding: 0; }
  html, body { width: 1200px; height: 915px; overflow: hidden; }
  body {
    background: var(--bg);
    position: relative;
    font-family: "Fredoka", sans-serif;
  }
  .label {
    position: absolute;
    top: 235px;
    width: 480px;
    height: 445px;
    background: var(--label-white);
    border-radius: 6px;
    overflow: hidden;
    box-shadow: 0 6px 24px rgba(40, 80, 100, 0.12);
  }
  .label--shampoo { left: 90px; }
  .label--bodywash { left: 630px; }

  .brand {
    position: absolute;
    top: 26px;
    left: 0;
    right: 0;
    text-align: center;
    font-weight: 700;
    font-size: 46px;
    letter-spacing: 1px;
    color: var(--brand-ink);
    line-height: 1;
  }

  .bubbles { position: absolute; inset: 0; pointer-events: none; }

  .mascot {
    position: absolute;
    left: 140px;
    top: 100px;
    width: 200px;
    height: 200px;
    border-radius: 48% 48% 40% 40%;
    background: radial-gradient(circle at 50% 40%, var(--bear-light), var(--bear-mid));
  }

  .volume {
    position: absolute;
    left: 22px;
    top: 192px;
    width: 110px;
    z-index: 1;
  }
  .volume__size {
    font-weight: 600;
    font-size: 28px;
    line-height: 1;
  }
  .volume__note {
    margin-top: 6px;
    font-family: "Tenor Sans", sans-serif;
    font-size: 11px;
    line-height: 1.2;
    color: #4a2a3a;
    text-transform: uppercase;
  }

  .claims {
    position: absolute;
    right: 20px;
    top: 118px;
    width: 110px;
    text-align: center;
  }
  .claims__top {
    font-weight: 600;
    font-size: 19px;
    line-height: 1.05;
  }
  .claims__pill {
    display: inline-block;
    margin: 8px 0 6px;
    padding: 6px 16px;
    border-radius: 30px;
    color: var(--text-white);
    font-weight: 600;
    font-size: 26px;
    line-height: 1;
  }
  .claims__bottom {
    font-weight: 600;
    font-size: 15px;
  }

  .band {
    position: absolute;
    left: 0; right: 0; bottom: 0;
    height: 160px;
  }
  .band__wave { position: absolute; top: -40px; left: 0; width: 100%; height: 60px; }
  .band__title {
    position: absolute;
    top: 22px;
    left: 0; right: 0;
    text-align: center;
    font-weight: 700;
    font-size: 54px;
    color: var(--text-white);
    line-height: 1;
  }
  .band__line {
    position: absolute;
    top: 96px;
    left: 0; right: 0;
    text-align: center;
    font-family: "Tenor Sans", sans-serif;
    font-size: 22px;
    letter-spacing: 0.5px;
    color: var(--text-white);
  }

  .label--shampoo .volume__size,
  .label--shampoo .claims__top,
  .label--shampoo .claims__bottom { color: var(--plum); }
  .label--shampoo .claims__pill { background: var(--plum); }
  .label--shampoo .band { background: var(--plum-band); }

  .label--bodywash .volume__size,
  .label--bodywash .claims__top,
  .label--bodywash .claims__bottom { color: var(--cyan-deep); }
  .label--bodywash .claims__pill { background: var(--cyan); }
  .label--bodywash .band { background: var(--cyan-band); }
</style>
</head>
<body>

<section class="label label--shampoo">
  <div class="brand">vellorine</div>
  <svg class="bubbles" viewBox="0 0 480 445" aria-hidden="true">
    <g fill="var(--pink-dot)">
      <circle cx="115" cy="120" r="9"/>
      <circle cx="70" cy="148" r="11"/>
      <circle cx="116" cy="172" r="12"/>
      <circle cx="42" cy="114" r="6"/>
      <circle cx="360" cy="238" r="9"/>
    </g>
  </svg>
  <div class="mascot" role="img" aria-label="Illustration of a smiling teddy bear with a blue ribbon"></div>
  <div class="volume">
    <div class="volume__size">250ml</div>
    <div class="volume__note">For oily &amp;<br>normal<br>hair types</div>
  </div>
  <div class="claims">
    <div class="claims__top">Collagen<br>&amp;</div>
    <div class="claims__pill">6 IN 1</div>
    <div class="claims__bottom">Essentials</div>
  </div>
  <div class="band">
    <svg class="band__wave" viewBox="0 0 480 60" preserveAspectRatio="none" aria-hidden="true">
      <path d="M0 40 C120 10 220 50 320 30 C400 14 450 20 480 28 L480 60 L0 60 Z" fill="var(--plum-band)"/>
    </svg>
    <div class="band__title">Shampoo</div>
    <div class="band__line">VELLORINE HERBAL REFRESHING</div>
  </div>
</section>

<section class="label label--bodywash">
  <div class="brand">vellorine</div>
  <svg class="bubbles" viewBox="0 0 480 445" aria-hidden="true">
    <g fill="var(--blue-dot)">
      <circle cx="120" cy="115" r="10"/>
      <circle cx="75" cy="145" r="8"/>
      <circle cx="112" cy="172" r="12"/>
      <circle cx="42" cy="112" r="6"/>
      <circle cx="360" cy="238" r="9"/>
    </g>
  </svg>
  <div class="mascot" role="img" aria-label="Illustration of a smiling teddy bear with a blue ribbon"></div>
  <div class="volume">
    <div class="volume__size">250ml</div>
    <div class="volume__note">For<br>everyday<br>use</div>
  </div>
  <div class="claims">
    <div class="claims__top">Collagen<br>&amp;</div>
    <div class="claims__pill">7 IN 1</div>
    <div class="claims__bottom">Essentials</div>
  </div>
  <div class="band">
    <svg class="band__wave" viewBox="0 0 480 60" preserveAspectRatio="none" aria-hidden="true">
      <path d="M0 40 C120 10 220 50 320 30 C400 14 450 20 480 28 L480 60 L0 60 Z" fill="var(--cyan-band)"/>
    </svg>
    <div class="band__title">Body Wash</div>
    <div class="band__line">VELLORINE HERBAL NOURISHING</div>
  </div>
</section>

</body>
</html>
```